Bright Meadow Counseling Business Card design with a visually interesting use of Space

I need business cards that are luxurious and give a peaceful, calm vibe. I also had some letterhead designed, and i like the look of it also, it's attached with the logo design for reference/ ideas but feel free to be creative.

Target Market(s)

High end luxurious client who needs counseling

Industry/Entity Type

Marriage and Family Therapy

Contact Information for Business Card

Mira Kowalczyk MS LMFT/ or Toby Hallett address 4150 Larkin Suite 600

Font styles to use
Sans Serif

Colors
0054AA
0677BA
7BADD7
CADEEF
E8F1F8
0094D4
00A9DD
6FCCEA
C7EBF8
E9F6FB
A7469A
B969AE
D3A5CF
EDDBEB
F8F0F9
6B429C
8869AF
B7A5CE
E3DAEB
F3F0F8

Requirements
Must have
• Logo and color scheme but be simple modern and luxurious
Nice to have
• I'd like to incorporate some elelmets from the logo and letterhead into a simple modern card

```html
<!DOCTYPE html>
<html lang="en">
<head>
<meta charset="utf-8">
<title>Bright Meadow Counseling – Business Card</title>
<link rel="stylesheet" href="https://fonts.googleapis.com/css2?family=Raleway:wght@300;400&display=swap">
<style>
  :root {
    --backdrop: #e6e4e8;
    --paper: #ffffff;
    --ink: #1d1d22;
    --violet: #6b53ae;
    --violet-line: #8a7cc4;
    --grad-start: #6e59b0;
    --grad-mid: #3a78a8;
    --grad-end: #079e99;
    --wash-blue: #e8f1f8;
    --wash-pink: #f8f0f9;
    --wash-mint: #e9f6fb;
  }
  * { box-sizing: border-box; margin: 0; padding: 0; }
  html, body {
    width: 1200px; height: 900px; overflow: hidden;
    background: var(--backdrop);
    font-family: "Raleway", sans-serif;
  }
  .stage { position: relative; width: 1200px; height: 900px; }
  .card {
    position: absolute; left: 250px; width: 700px; height: 400px;
    border-radius: 22px; overflow: hidden;
    box-shadow: 0 10px 28px rgba(0,0,0,0.18);
  }
  .card-front {
    top: 40px;
    background: linear-gradient(100deg, var(--grad-start) 0%, var(--grad-mid) 50%, var(--grad-end) 100%);
    display: flex; align-items: center; justify-content: center;
  }
  .card-back { top: 470px; background: var(--paper); }

  .wordmark { text-align: right; line-height: 1; font-weight: 300; }
  .wordmark-name { display: block; font-size: 54px; letter-spacing: 1px; }
  .wordmark-tag { display: block; font-size: 26px; letter-spacing: 6px; margin-top: 4px; }
  .card-front .wordmark { color: #ffffff; }
  .card-back .wordmark { color: var(--ink); position: absolute; left: 70px; top: 90px; }
  .card-back .wordmark-name { font-size: 40px; }
  .card-back .wordmark-tag { font-size: 19px; letter-spacing: 5px; }

  .backdrop-wash {
    position: absolute; right: -40px; top: -30px; width: 420px; height: 300px;
    background: radial-gradient(ellipse at 40% 50%, var(--wash-pink) 0%, var(--wash-blue) 45%, var(--wash-mint) 65%, rgba(255,255,255,0) 80%);
  }

  .person { position: absolute; right: 60px; top: 92px; text-align: right; }
  .person-name { color: var(--violet); font-size: 26px; font-weight: 400; letter-spacing: 1px; text-transform: uppercase; }
  .person-role { color: var(--ink); font-size: 17px; font-weight: 400; margin-top: 2px; letter-spacing: .5px; }

  .divider {
    position: absolute; left: 150px; right: 40px; top: 216px;
    height: 1px; background: var(--violet-line);
  }

  .contact { position: absolute; left: 150px; top: 236px; list-style: none; }
  .contact li { display: flex; align-items: center; gap: 10px; font-size: 17px; color: var(--ink); margin-bottom: 6px; }
  .contact svg { width: 16px; height: 16px; flex: none; }

  .portal { position: absolute; right: 60px; bottom: 64px; font-size: 17px; color: var(--ink); }
  .accent-bar {
    position: absolute; right: 0; bottom: 26px; width: 360px; height: 14px;
    background: var(--violet);
  }
</style>
</head>
<body>
<main class="stage">
  <section class="card card-front">
    <div class="wordmark">
      <span class="wordmark-name">Bright Meadow</span>
      <span class="wordmark-tag">Counseling</span>
    </div>
  </section>

  <section class="card card-back">
    <div class="backdrop-wash" role="img" aria-label="Soft pastel wash of blue, pink and mint"></div>

    <div class="wordmark">
      <span class="wordmark-name">Bright Meadow</span>
      <span class="wordmark-tag">Counseling</span>
    </div>

    <div class="person">
      <p class="person-name">Mira Kowalczyk</p>
      <p class="person-role">Therapist and Consultant</p>
    </div>

    <div class="divider"></div>

    <ul class="contact">
      <li>
        <svg viewBox="0 0 24 24" aria-hidden="true"><path fill="#6b53ae" d="M6.6 10.8a15 15 0 0 0 6.6 6.6l2.2-2.2a1 1 0 0 1 1-.25 11.4 11.4 0 0 0 3.6.57 1 1 0 0 1 1 1V20a1 1 0 0 1-1 1A17 17 0 0 1 3 4a1 1 0 0 1 1-1h3.5a1 1 0 0 1 1 1c0 1.25.2 2.45.57 3.57a1 1 0 0 1-.25 1z"/></svg>
        310.555.0148
      </li>
      <li>
        <svg viewBox="0 0 24 24" aria-hidden="true"><rect x="2.5" y="5" width="19" height="14" rx="1.5" fill="none" stroke="#6b53ae" stroke-width="2"/><path d="M3 6l9 7 9-7" fill="none" stroke="#6b53ae" stroke-width="2"/></svg>
        info@mirakowalczyk.com
      </li>
    </ul>

    <p class="portal">mira-kowalczyk.clientportal.me</p>
    <div class="accent-bar"></div>
  </section>
</main>
</body>
</html>
```